Corbin Lantern Lighting - Commercial & Residential Landscape Lighting

Landscape Lighting Services & Design: Create a website for our landscape lighting company. We would like the design to be tailored around this description:
Illuminate with Confidence. Designed with Precision. Installed with Care.
Locally and veteran-owned, we take pride in transforming outdoor spaces through innovative lighting solutions tailored to your vision. From landscape and holiday lighting to permanent installations, our effortless process and expert design deliver breathtaking results and lasting curb appeal. Backed by a lifetime warranty and quarterly service options, our commitment to quality and customer satisfaction is unwavering. Try before you buy and experience your home in a whole new light with our complimentary demo kit — see the stunning effects before you decide.
- Also, add in this information as well; Outdoor Lighting not only beautifies spaces but also significantly enhances safety by illuminating your home or business. Beautifully lit entrances deter potential intruders, making your home a safer place for your loved ones. we also offer quarterly service plans to ensure lighting equipment continues to operate & illuminate effectively throughout the year. Also mention we provide free estimates and we are offering a 10% discount to military, veterans, and first responders.

Target Market(s)

Luxury market

Industry/Entity Type

Landscape Lighting - Residential & Commercial Lighting Services

Coding

Coded - Design and coding required

Number of Pages Required

2 page

Colors
00AB8E
00BBA5
67D7C9
C6EFE9
E9F9F6
59FF00
82FF00
B8FF75
E3FFCB
F4FFEA
FFC000
F8CF3A
FAE287
FDF2CF
FEFAEE

Requirements
Must have
• a lead generation button where people can submit their information for us to reach out to them and schedule their free estimate, homepage, about page, contact page, products and services page, user friendly, easy to navigate, and it also must be engaging and eye popping, as well as appealing to the luxury market. Please use colors; verdent green, dark green, ivory, and sunny yellow. Also, include an about page that references our story; Derek is retired Army and he opened a fitness studio in 2017 with his wife Vanessa. He has installed low voltage lighting in every home he lived in and for his friends and family over the years and decided to open his own business because he is passionate about beautifying outdoor landscapes and highlighting a properties full potential, not only in the day but at night as well all while providing safety and security for his clients. Having a deep respect for nature and landscaping, he wants to provide the same care and quality to each of his clients as he has in the fitness industry for decades. He believes small businesses are the back bone of America and he's excited to provide a service that is all to often neglected in the design of a home.
Nice to have
• I would like to have a clear intent and purpose, engaging web design, clear call to action, optimized for search engines, mobile friendy design, security measures, credibility indicators

```html
<!DOCTYPE html>
<html lang="en">
<head>
<meta charset="utf-8">
<title>Corbin Lantern Lighting – Residential &amp; Commercial Landscape Lighting</title>
<link rel="stylesheet" href="https://fonts.googleapis.com/css2?family=Montserrat:wght@400;500;600;700&display=swap">
<style>
:root{
  --black:#050505;
  --ink:#0b0b0b;
  --gold:#f6b93b;
  --gold-soft:#f8cf3a;
  --gold-pale:#fae287;
  --amber:#d9963a;
  --teal:#00ab8e;
  --teal-deep:#0d7f67;
  --forest:#0f3b2b;
  --forest-2:#163f30;
  --ivory:#fefaee;
  --text:#e9e5da;
  --muted:#bdb8aa;
}
*{box-sizing:border-box;margin:0;padding:0}
html,body{width:1200px;height:4979px;overflow:hidden;background:var(--black)}
body{font-family:"Montserrat",Arial,sans-serif;color:var(--text);position:relative}
.abs{position:absolute}
.btn{position:absolute;display:flex;align-items:center;justify-content:center;border-radius:30px;font-weight:600;font-size:15px;letter-spacing:.5px;text-transform:uppercase;color:#1a1305;background:linear-gradient(90deg,#f3a93a,#f8cf3a);text-decoration:none}
.btn-teal{background:linear-gradient(90deg,#00ab8e,#00bba5);color:#fff}
.btn-line{background:transparent;border:2px solid #fff;color:#fff}
.btn-line.dark{border-color:#2a2010;color:#2a2010}
.eyebrow{font-size:15px;letter-spacing:3px;text-transform:uppercase;color:#fff}
.title{font-weight:500;text-transform:uppercase;line-height:1.15;color:var(--gold-pale);background:linear-gradient(90deg,#fbe29a,#e9a43a);-webkit-background-clip:text;background-clip:text;-webkit-text-fill-color:transparent}
.underline{position:absolute;height:3px;background:linear-gradient(90deg,transparent,#e9a43a,transparent)}
p.body{font-size:17px;line-height:1.62;color:var(--text)}
.photo{position:absolute}

/* header */
.nav a{position:absolute;top:60px;font-size:14px;letter-spacing:.5px;text-transform:uppercase;color:#fff;text-decoration:none}
.brand{position:absolute;text-align:center;font-weight:500;color:var(--gold);text-transform:uppercase}
.brand .name{font-size:40px;letter-spacing:6px;line-height:1}
.brand .tag{font-size:13px;letter-spacing:4px;margin-top:6px}

/* hero */
.hero{left:0;top:0;width:1200px;height:760px;background:
 radial-gradient(ellipse at 18% 62%,rgba(226,140,60,.55),transparent 38%),
 radial-gradient(ellipse at 80% 55%,rgba(210,120,60,.5),transparent 35%),
 radial-gradient(ellipse at 50% 35%,#1b2a33,transparent 70%),
 linear-gradient(180deg,#0f1a22 0%,#1a1f1c 45%,#10140f 75%,#050505 100%)}
.hero-title{position:absolute;left:0;width:1200px;top:202px;text-align:center;font-size:40px;font-weight:500;line-height:51px;letter-spacing:1px;text-transform:uppercase;color:var(--gold-pale);background:linear-gradient(90deg,#fbe9b0,#e9a43a 50%,#fbe9b0);-webkit-background-clip:text;background-clip:text;-webkit-text-fill-color:transparent}

/* about */
.quote{position:absolute;left:614px;top:1128px;width:560px;padding-left:22px;border-left:2px solid var(--gold);font-size:19px;font-weight:700;line-height:1.42;color:var(--gold-soft)}
.card{position:absolute;top:1331px;height:138px;display:flex;align-items:center;gap:20px;padding-left:34px}
.card .ic{width:80px;height:80px;border-radius:50%;display:flex;align-items:center;justify-content:center;flex:none}
.card h3{font-size:19px;font-weight:500;text-transform:uppercase;color:#fff}
.card p{font-size:15px;text-transform:uppercase;color:#fff;line-height:1.25;margin-top:6px}

/* split */
.panel{top:1532px;width:600px;height:462px;text-align:center}
.panel h2{position:absolute;left:0;width:600px;top:120px;font-size:33px;font-weight:500;line-height:39px;text-transform:uppercase}
.panel p{position:absolute;left:90px;width:420px;top:232px;font-size:16px;line-height:1.6}

/* products */
.circ{position:absolute;width:340px;height:340px;border-radius:50%;overflow:hidden}
.circ .lbl{position:absolute;left:0;width:100%;text-align:center;font-size:22px;font-weight:600;line-height:28px;text-transform:uppercase}
.circ .lbl span{display:block;color:var(--gold)}

/* form */
.field{position:absolute;height:50px;border:1px solid rgba(255,255,255,.25);border-radius:4px;background:rgba(0,0,0,.35);display:flex;align-items:center;padding-left:20px;gap:12px;font-size:14px;color:#fff}
.field.area{height:118px;align-items:flex-start;padding-top:16px}

/* footer */
.fnav{position:absolute;top:4758px;font-size:13px;font-weight:600;text-transform:uppercase;color:#fff}
.dot{position:absolute;top:4764px;width:5px;height:5px;border-radius:50%;background:var(--gold)}
.contact-item{position:absolute;top:4845px;display:flex;align-items:center;gap:16px;font-size:13px;color:#fff}
.contact-item .ic{width:36px;height:36px;border-radius:50%;background:var(--gold);display:flex;align-items:center;justify-content:center}
.social{position:absolute;top:4852px;width:26px;height:26px;border-radius:50%;border:2px solid var(--gold)}
</style>
</head>
<body>

<!-- HERO -->
<section class="abs hero" role="img" aria-label="Brick home at dusk with warm landscape lighting along the lawn and driveway"></section>
<nav class="nav">
  <a style="left:140px">Home</a>
  <span class="abs" style="left:140px;top:88px;width:46px;height:2px;background:#fff"></span>
  <a style="left:234px">About</a>
  <a style="left:336px">Services</a>
  <a style="left:750px">Products</a>
  <a style="left:882px">Contact Us</a>
</nav>
<div class="brand" style="left:470px;top:34px;width:260px">
  <div class="name">Corbin</div>
  <div class="tag">Lantern Lighting</div>
</div>
<a class="btn" style="left:1016px;top:48px;width:154px;height:38px;font-size:12px">Free Estimate ›</a>
<h1 class="hero-title">Illuminate with confidence.<br>Designed with precision.<br>Installed with care.</h1>
<a class="btn btn-teal" style="left:510px;top:390px;width:180px;height:44px;font-size:13px">Free Estimate ›</a>
<svg class="abs" style="left:0;top:600px" width="1200" height="160" viewBox="0 0 1200 160">
  <path d="M0 160 L0 120 Q600 0 1200 120 L1200 160 Z" fill="#050505"/>
  <path d="M130 98 Q600 -8 1070 98" fill="none" stroke="#e9a43a" stroke-width="4"/>
</svg>

<!-- ABOUT -->
<div class="photo" style="left:145px;top:841px;width:424px;height:424px;border-radius:50%;background:radial-gradient(circle at 50% 35%,#556b48,#2c3a23 55%,#6b5a1c 100%);border:3px solid #c9923a" role="img" aria-label="Lit home with manicured lawn framed in a circle"></div>
<div class="eyebrow abs" style="left:618px;top:780px">Who we are</div>
<h2 class="title abs" style="left:614px;top:802px;font-size:38px;width:560px">About Corbin<br>Lantern Lighting</h2>
<p class="body abs" style="left:616px;top:922px;width:540px;font-size:16px;line-height:1.7">Locally and veteran-owned, we take pride in transforming outdoor spaces through innovative lighting solutions tailored to your vision. From landscape and holiday lighting to permanent installations, our effortless process and expert design deliver breathtaking results and lasting curb appeal. Backed by a lifetime warranty and quarterly service options, our commitment to quality and customer satisfaction is unwavering.</p>
<div class="quote">Try before you buy and experience your home in a whole new light with our complimentary demo kit see the stunning effects before you decide.</div>
<a class="btn" style="left:620px;top:1236px;width:180px;height:44px;font-size:14px">Learn More ›</a>

<div class="card" style="left:120px;width:466px;border:1px solid var(--teal-deep)">
  <div class="ic" style="background:var(--teal)">
    <svg width="40" height="40" viewBox="0 0 40 40" fill="none" stroke="#fff" stroke-width="2.4"><rect x="9" y="5" width="22" height="30" rx="2"/><path d="M14 13h12M14 19h12M14 25h8"/></svg>
  </div>
  <div><h3>We provide free estimate</h3><p>Get a free estimate now</p></div>
</div>
<div class="card" style="left:612px;width:466px;border:1px solid #b8862e">
  <div class="ic" style="background:var(--gold)">
    <svg width="40" height="40" viewBox="0 0 40 40" fill="none" stroke="#2a1d05" stroke-width="2.4"><path d="M13 4l7 10 7-10"/><circle cx="20" cy="25" r="10"/><path d="M20 19l2 4 4 .5-3 3 .8 4-3.8-2-3.8 2 .8-4-3-3 4-.5z"/></svg>
  </div>
  <div><h3>We offering a 10% discount</h3><p>To military, veterans, and<br>first responders</p></div>
</div>

<!-- RESIDENTIAL / COMMERCIAL -->
<section class="abs panel" style="left:0;background:linear-gradient(135deg,#0c5a45,#11866a 55%,#1a9e7c);color:#fff" role="img" aria-label="Garden steps lit at night under a green tint">
  <h2>Residential<br>Landscape Lighting</h2>
  <p>Lorem ipsum dolor sit amet, consectetur adipiscing elit, sed do eiusmod tempor incididun</p>
  <a class="btn btn-line" style="left:230px;top:310px;width:180px;height:44px;font-size:13px">Learn More ›</a>
</section>
<section class="abs panel" style="left:600px;background:linear-gradient(135deg,#f6c64a,#f8d36a 50%,#f3c7a4);color:#2a2010" role="img" aria-label="Commercial building and terrace lit at dusk under a golden tint">
  <h2>Commercial<br>Landscape Lighting</h2>
  <p>Lorem ipsum dolor sit amet, consectetur adipiscing elit, sed do eiusmod tempor incididun</p>
  <a class="btn btn-line dark" style="left:220px;top:310px;width:180px;height:44px;font-size:13px">Learn More ›</a>
</section>

<!-- PRODUCTS & SERVICES -->
<section class="abs" style="left:0;top:1994px;width:1200px;height:692px;background:radial-gradient(ellipse at 50% 85%,#5a3f12,transparent 60%),linear-gradient(180deg,#050505 0%,#121a12 45%,#2a2310 80%,#0a0a0a 100%)" role="img" aria-label="Backyard patio and lawn lit warmly at night"></section>
<div class="eyebrow abs" style="left:0;width:1200px;top:2080px;text-align:center;font-size:14px">What we do</div>
<h2 class="title abs" style="left:0;width:1200px;top:2098px;text-align:center;font-size:38px">Products &amp; Services</h2>
<div class="underline" style="left:465px;top:2152px;width:270px"></div>

<div class="circ" style="left:77px;top:2226px;background:radial-gradient(circle at 50% 40%,#3f5a2a,#1b2b15 70%)" role="img" aria-label="Garden path with landscape lights">
  <div class="lbl" style="top:238px;color:#fff"><span>Landscape</span>Lighting</div>
</div>
<div class="circ" style="left:435px;top:2226px;background:#10523c;border:3px solid var(--gold);color:#fff">
  <div class="lbl" style="top:80px;color:#fff"><span>Holiday</span>Lighting</div>
  <p class="abs" style="left:58px;width:224px;top:150px;text-align:center;font-size:12px;line-height:1.6">Lorem ipsum dolor sit amet, consectetur adipiscing elit, sed do eiusmod tempor incididunt ut labore et dolore magna aliqua.</p>
  <a class="btn" style="left:105px;top:244px;width:130px;height:32px;font-size:11px">Learn More ›</a>
</div>
<div class="circ" style="left:792px;top:2226px;background:radial-gradient(circle at 40% 50%,#6a6250,#27313e 55%,#1a2233)" role="img" aria-label="Two storey house with permanent facade lighting">
  <div class="lbl" style="top:236px;color:#fff"><span>Permanent</span>Installations</div>
</div>

<!-- WHY OUTDOOR LIGHTING -->
<div class="eyebrow abs" style="left:126px;top:2764px">Outdoor Lighting</div>
<h2 class="title abs" style="left:124px;top:2784px;font-size:38px;width:480px">Why Outdoor<br>Lighting</h2>
<div class="underline" style="left:124px;top:2890px;width:160px;background:linear-gradient(90deg,#e9a43a,transparent)"></div>
<p class="body abs" style="left:122px;top:2918px;width:460px">Outdoor Lighting not only beautifies spaces but also significantly enhances safety by illuminating your home or business.</p>
<p class="body abs" style="left:122px;top:3028px;width:420px">Beautifully lit entrances deter potential intruders, making your home a safer place for your loved ones. We also offer quarterly service plans to ensure lighting equipment continues to operate &amp; illuminate effectively throughout the year.</p>
<a class="btn" style="left:120px;top:3218px;width:206px;height:50px;font-size:15px">Free Estimate ›</a>
<div class="photo" style="left:653px;top:2780px;width:464px;height:435px;border-radius:12px;background:linear-gradient(180deg,#2b3a48 0%,#5a5040 45%,#3d4a2a 75%,#5d5a3c 100%)" role="img" aria-label="Brick home with uplit gable and front lawn at dusk"></div>
<div class="photo" style="left:568px;top:3072px;width:302px;height:241px;border:2px solid #fff;background:linear-gradient(180deg,#123b70 0%,#1f4c7e 40%,#7a5a38 70%,#3c3a36 100%)" role="img" aria-label="Modern house with lit driveway under a blue evening sky"></div>

<!-- DEMO KIT -->
<div class="photo" style="left:83px;top:3479px;width:472px;height:472px;border-radius:50%;border:4px solid #fff;box-shadow:0 0 0 8px #050505,0 0 0 10px #fff;background:linear-gradient(180deg,#0d3a8a 0%,#2458a8 40%,#b07a3a 65%,#3f5a2a 100%)" role="img" aria-label="Lit two storey home under a deep blue evening sky"></div>
<div class="eyebrow abs" style="left:627px;top:3498px;font-size:14px">Our demo kit</div>
<h2 class="title abs" style="left:625px;top:3518px;font-size:38px;width:520px">Our Complimentary<br>Demo Kit</h2>
<p class="body abs" style="left:627px;top:3658px;width:500px">Experience the Transformation - Before You Commit - Smaller writing below that: See your property in a whole new light with our Complimentary Demo Kit. We'll design and install a temporary lighting setup so you can witness the beauty, safety, and curb appeal first hand - all at no cost.</p>
<a class="btn" style="left:624px;top:3862px;width:288px;height:50px;font-size:15px">Get My Free Demo Kit ›</a>

<!-- CONTACT -->
<section class="abs" style="left:0;top:4038px;width:1200px;height:638px;background:radial-gradient(ellipse at 7% 45%,rgba(250,220,140,.45),transparent 18%),linear-gradient(180deg,#050505 0%,#1a2418 30%,#23301c 70%,#0b0d09 100%)" role="img" aria-label="Garden lantern post glowing beside a lawn at night"></section>
<div class="abs" style="left:131px;top:4105px;width:945px;height:555px;border-radius:14px;background:rgba(14,70,48,.92);border:1px solid rgba(255,255,255,.12)"></div>
<div class="eyebrow abs" style="left:0;width:1200px;top:4176px;text-align:center;font-size:14px;color:var(--gold)">Contact us</div>
<h2 class="title abs" style="left:0;width:1200px;top:4194px;text-align:center;font-size:34px">Schedule Free Estimate</h2>
<div class="field" style="left:234px;top:4260px;width:360px">
  <svg width="14" height="14" viewBox="0 0 14 14" fill="#fff"><circle cx="7" cy="4" r="3.2"/><path d="M1 14c0-4 2.7-6 6-6s6 2 6 6z"/></svg>First Name</div>
<div class="field" style="left:606px;top:4260px;width:360px">
  <svg width="14" height="14" viewBox="0 0 14 14" fill="#fff"><circle cx="7" cy="4" r="3.2"/><path d="M1 14c0-4 2.7-6 6-6s6 2 6 6z"/></svg>Last Name</div>
<div class="field" style="left:234px;top:4322px;width:360px">
  <svg width="14" height="12" viewBox="0 0 14 12" fill="none" stroke="#fff" stroke-width="1.6"><rect x="1" y="1" width="12" height="10"/><path d="M1 1l6 5 6-5"/></svg>Email address</div>
<div class="field" style="left:606px;top:4322px;width:360px">
  <svg width="14" height="14" viewBox="0 0 14 14" fill="#fff"><path d="M3 1l2.5 3-1.5 2c1 2 2 3 4 4l2-1.5 3 2.5-1.5 2.5C6 13 1 8 .5 2.5z"/></svg>Phone number</div>
<div class="field area" style="left:234px;top:4384px;width:732px">
  <svg width="14" height="14" viewBox="0 0 14 14" fill="#fff"><path d="M7 1C3 1 .5 3.4.5 6c0 1.6.9 3 2.3 3.9L2 13l3.4-2.2c.5.1 1 .2 1.6.2 4 0 6.5-2.4 6.5-5S11 1 7 1z"/></svg>Leave Message</div>
<a class="btn" style="left:496px;top:4534px;width:208px;height:48px;font-size:15px">Send Message ›</a>

<!-- FOOTER -->
<div class="abs" style="left:60px;top:4724px;width:1080px;height:1px;background:rgba(255,255,255,.15)"></div>
<span class="fnav" style="left:142px">Home</span>
<span class="dot" style="left:226px"></span>
<span class="fnav" style="left:255px">About us</span>
<span class="dot" style="left:366px"></span>
<span class="fnav" style="left:398px">Services</span>
<div class="brand" style="left:488px;top:4738px;width:230px">
  <div class="name" style="font-size:36px">Corbin</div>
  <div class="tag" style="font-size:12px">Lantern Lighting</div>
</div>
<span class="fnav" style="left:736px">Products</span>
<span class="dot" style="left:848px"></span>
<span class="fnav" style="left:885px">Gallery</span>
<span class="dot" style="left:982px"></span>
<span class="fnav" style="left:1016px">Contact</span>

<div class="contact-item" style="left:130px">
  <span class="ic"><svg width="14" height="18" viewBox="0 0 14 18" fill="#fff"><path d="M7 0a7 7 0 0 0-7 7c0 5 7 11 7 11s7-6 7-11a7 7 0 0 0-7-7zm0 9.5A2.5 2.5 0 1 1 7 4.5a2.5 2.5 0 0 1 0 5z"/></svg></span>123 Street Address line</div>
<div class="contact-item" style="left:412px">
  <span class="ic"><svg width="16" height="16" viewBox="0 0 14 14" fill="#fff"><path d="M3 1l2.5 3-1.5 2c1 2 2 3 4 4l2-1.5 3 2.5-1.5 2.5C6 13 1 8 .5 2.5z"/></svg></span>(555) 014-2286</div>
<div class="contact-item" style="left:612px">
  <span class="ic"><svg width="16" height="12" viewBox="0 0 14 12" fill="none" stroke="#fff" stroke-width="1.6"><rect x="1" y="1" width="12" height="10"/><path d="M1 1l6 5 6-5"/></svg></span>hello@corbinlantern.com</div>
<span class="social" style="left:934px"></span>
<span class="social" style="left:972px"></span>
<span class="social" style="left:1010px"></span>
<span class="social" style="left:1048px"></span>

<div class="abs" style="left:0;top:4932px;width:1200px;height:47px;background:#1b1b1b;display:flex;align-items:center;justify-content:center;font-size:12px;color:#bdb8aa">Copyright © 2025 Corbin Lantern | All Right Reserved</div>

</body>
</html>
```